Bramwell Business Cards

Logo files are included. Full "Bramwell" logo should be included on the back of the business card. The B symbol should be included on the front with the contact information.

Bramwell, LLC is the company name and we do commercial construction and real estate development consulting services. Look for a fairly simple card design utilizing our logo.

```html
<!DOCTYPE html>
<html lang="en">
<head>
<meta charset="utf-8">
<title>Bramwell Business Cards</title>
<link rel="stylesheet" href="https://fonts.googleapis.com/css2?family=Montserrat:wght@400;600;700&display=swap">
<style>
  :root {
    --navy: #1b384d;
    --gold: #ebac06;
    --ink-soft: #8a8d90;
    --paper: #ffffff;
    --stage: #2a2a2c;
  }
  * { box-sizing: border-box; margin: 0; padding: 0; }
  html, body {
    width: 1200px; height: 1024px; overflow: hidden;
    background: var(--stage);
    font-family: "Montserrat", sans-serif;
  }
  .sheet {
    width: 1200px; height: 1024px;
    display: flex; flex-direction: column; align-items: center; justify-content: center;
    gap: 56px;
  }
  .card {
    position: relative;
    width: 700px; height: 400px;
    background: var(--paper);
    overflow: hidden;
    box-shadow: 0 10px 30px rgba(0,0,0,.45);
  }

  /* back of card */
  .card--back { display: flex; align-items: center; justify-content: center; gap: 22px; }
  .card--back .brand-dot {
    width: 64px; height: 64px; border-radius: 50%; background: var(--gold);
  }
  .card--back .brand-name {
    font-weight: 600; font-size: 62px; letter-spacing: 3px; color: var(--navy);
  }

  /* front of card */
  .holder {
    position: absolute; top: 52px; right: 50px; text-align: right;
  }
  .holder-name { font-weight: 700; font-size: 30px; letter-spacing: 1px; }
  .holder-name .first { color: var(--navy); }
  .holder-name .last { color: var(--gold); }
  .holder-role { font-size: 15px; color: var(--ink-soft); margin-top: 2px; }

  .front-brand {
    position: absolute; left: 50px; top: 150px;
    display: flex; align-items: center; gap: 14px;
  }
  .front-brand .brand-dot {
    width: 38px; height: 38px; border-radius: 50%; border: 4px solid var(--navy);
  }
  .front-brand .brand-name {
    font-weight: 600; font-size: 38px; letter-spacing: 2px; color: var(--navy);
  }

  .contact {
    position: absolute; left: 50px; bottom: 40px;
    font-size: 15px; color: var(--ink-soft); line-height: 1.45;
  }
  .contact address { font-style: normal; margin-bottom: 10px; }
  .contact ul { list-style: none; }
  .contact li { display: flex; align-items: center; gap: 10px; margin-top: 4px; }
  .contact svg { width: 18px; height: 18px; flex: none; }
</style>
</head>
<body>
<main class="sheet">

  <section class="card card--back" aria-label="Business card back">
    <span class="brand-dot" aria-hidden="true"></span>
    <span class="brand-name">BRAMWELL</span>
  </section>

  <section class="card card--front" aria-label="Business card front">
    <div class="holder">
      <p class="holder-name"><span class="first">DANA</span> <span class="last">WHITFIELD</span></p>
      <p class="holder-role">CEO/Owner</p>
    </div>

    <div class="front-brand">
      <span class="brand-dot" aria-hidden="true"></span>
      <span class="brand-name">BRAMWELL</span>
    </div>

    <div class="contact">
      <address>48 Harbor Row, Suite 2,<br>Easton 00417</address>
      <ul>
        <li>
          <svg viewBox="0 0 20 20" aria-hidden="true"><circle cx="10" cy="10" r="10" fill="var(--gold)"/><path d="M6.5 5.5l2 .2.8 2-1.2 1a6 6 0 0 0 3.2 3.2l1-1.2 2 .8.2 2c-4.5.6-8.6-3.5-8-8z" fill="#fff"/></svg>
          (555) 214-0793
        </li>
        <li>
          <svg viewBox="0 0 20 20" aria-hidden="true"><circle cx="10" cy="10" r="10" fill="var(--gold)"/><rect x="5" y="6.5" width="10" height="7" rx="1" fill="#fff"/><path d="M5.5 7l4.5 3.5L14.5 7" fill="none" stroke="var(--gold)" stroke-width="1.2"/></svg>
          info@Bramwellllc.com
        </li>
        <li>
          <svg viewBox="0 0 20 20" aria-hidden="true"><circle cx="10" cy="10" r="10" fill="var(--gold)"/><g fill="none" stroke="#fff" stroke-width="1.1"><circle cx="10" cy="10" r="5"/><ellipse cx="10" cy="10" rx="2.2" ry="5"/><path d="M5 10h10"/></g></svg>
          www.Bramwellllc.com
        </li>
      </ul>
    </div>
  </section>

</main>
</body>
</html>
```